Graph Template Design

We are looking for a modern and flat theme of the attached image/graph/flowchart. It does not have to be in the same format or layout but needs to show the same flows.

We are a small digital agency based in Malta (Larkfen Hub). We service clients with online media and marketing strategies and the basis of this project is to use the design for a client proposal document which is being reworked.

Design Specifics: I have submitted my design and the specs inside the proposal. We are looking for a designer to redesign the attached image in our proposal set
up with you yesterday. I have submitted an existing design and also submitted my preferred colors etc. Please see the submission we made.

Target Market(s)

We are looking for designs to compliment oir business proposal for our new and existing clients.

Industry/Entity Type

Media

Font styles to use
Sans Serif

Colors
0555a3
3276b5
33a6d7
9bcb3b
85cae6
abd036

Requirements
Must have
• we need to keep the flow of the graph the same but it can be redesigned to make it look more modern etc
Nice to have
• flat design

```html
<!DOCTYPE html>
<html lang="en">
<head>
<meta charset="utf-8">
<title>Larkfen Hub – Media Flow</title>
<link href="https://fonts.googleapis.com/css2?family=Exo+2:wght@400;500;700;800&display=swap" rel="stylesheet">
<style>
  :root {
    --bg: #ffffff;
    --brand: #0555a3;
    --social: #3276b5;
    --portal: #9bcb3b;
    --bookmark: #3276b5;
    --channel: #33a6d7;
    --accent: #abd036;
    --soft: #85cae6;
    --ring: #85cae6;
    --flow: #a9c3d6;
    --label: #ffffff;
  }
  html, body { margin: 0; padding: 0; overflow: hidden; background: var(--bg); }
  .canvas { width: 1200px; height: 852px; display: block; font-family: "Exo 2", sans-serif; }
  .flow { fill: none; stroke: var(--flow); stroke-width: 2; stroke-dasharray: 5 4; }
  .arrowhead { fill: var(--flow); }
  .ring { fill: #fff; stroke: var(--ring); stroke-width: 3; }
  .brand-ring { fill: none; stroke: var(--brand); stroke-width: 1.6; }
  .brand-name { fill: var(--brand); font-weight: 800; font-size: 28px; text-anchor: middle; }
  .node-label { fill: var(--label); font-weight: 500; font-size: 16px; text-anchor: middle; }
  .channel circle.disc { fill: var(--channel); }
  .channel .glyph { fill: rgba(255,255,255,0.85); }
  .channel text { fill: var(--label); font-size: 7.2px; font-weight: 500; text-anchor: middle; }
  .port { stroke: #fff; stroke-width: 2; }
  .port-outline { fill: none; stroke: var(--ring); stroke-width: 1.5; }
  .port-brand { fill: var(--brand); }
  .port-social { fill: var(--social); }
  .port-portal { fill: var(--portal); }
  .port-channel { fill: var(--accent); }
</style>
</head>
<body>
<svg class="canvas" viewBox="0 0 1200 852" xmlns="http://www.w3.org/2000/svg">
  <defs>
    <marker id="arrow" viewBox="0 0 10 10" refX="8" refY="5" markerWidth="6" markerHeight="6" orient="auto-start-reverse">
      <path class="arrowhead" d="M0,0 L10,5 L0,10 z"/>
    </marker>
  </defs>

  <g class="flows">
    <path class="flow" marker-end="url(#arrow)" d="M187,321 C260,170 430,95 636,82"/>
    <path class="flow" marker-end="url(#arrow)" d="M645,108 C450,115 280,200 214,330"/>
    <path class="flow" marker-end="url(#arrow)" d="M187,527 C260,678 430,753 636,766"/>
    <path class="flow" marker-end="url(#arrow)" d="M645,740 C450,733 280,648 214,518"/>
    <path class="flow" marker-end="url(#arrow)" d="M486,238 L251,364"/>
    <path class="flow" marker-end="url(#arrow)" d="M615,194 L666,136"/>
    <path class="flow" marker-end="url(#arrow)" d="M257,412 L350,412"/>
    <path class="flow" marker-end="url(#arrow)" d="M357,440 L264,440"/>
    <path class="flow" marker-end="url(#arrow)" d="M479,358 L510,322"/>
    <path class="flow" marker-end="url(#arrow)" d="M479,491 L512,530"/>
    <path class="flow" marker-end="url(#arrow)" d="M486,614 L251,490"/>
    <path class="flow" marker-end="url(#arrow)" d="M615,654 L666,714"/>
    <path class="flow" marker-end="url(#arrow)" d="M942,424 L650,267"/>
    <path class="flow" marker-end="url(#arrow)" d="M942,424 L528,424"/>
    <path class="flow" marker-end="url(#arrow)" d="M942,424 L650,579"/>
  </g>

  <g class="brand">
    <circle class="brand-ring" cx="147" cy="424" r="110"/>
    <circle class="brand-ring" cx="147" cy="424" r="94"/>
    <text class="brand-name" x="147" y="434">Larkfen Hub</text>
  </g>

  <g class="hub hub-social">
    <circle class="ring" cx="562" cy="252" r="76"/>
    <circle cx="562" cy="252" r="64" fill="var(--social)"/>
    <rect role="img" aria-label="Social network megaphone icon" x="537" y="200" width="50" height="45" rx="8" fill="rgba(255,255,255,0.25)"/>
    <text class="node-label" x="562" y="286">Social Media</text>
  </g>
  <g class="hub hub-portal">
    <circle class="ring" cx="436" cy="424" r="80"/>
    <circle cx="436" cy="424" r="64" fill="var(--portal)"/>
    <rect role="img" aria-label="Browser window with gear icon" x="411" y="386" width="50" height="44" rx="6" fill="rgba(255,255,255,0.25)"/>
    <text class="node-label" x="436" y="458">News Portal</text>
  </g>
  <g class="hub hub-bookmark">
    <circle class="ring" cx="562" cy="596" r="76"/>
    <circle cx="562" cy="596" r="64" fill="var(--bookmark)"/>
    <rect role="img" aria-label="Award ribbon icon" x="542" y="554" width="40" height="50" rx="8" fill="rgba(255,255,255,0.25)"/>
    <text class="node-label" x="562" y="630">Bookmarking</text>
  </g>

  <g class="ports">
    <g><circle class="port-outline" cx="187" cy="321" r="9"/><circle class="port port-brand" cx="187" cy="321" r="7"/></g>
    <g><circle class="port-outline" cx="257" cy="412" r="9"/><circle class="port port-brand" cx="257" cy="412" r="7"/></g>
    <g><circle class="port-outline" cx="187" cy="527" r="9"/><circle class="port port-brand" cx="187" cy="527" r="7"/></g>
    <g><circle class="port-outline" cx="486" cy="238" r="9"/><circle class="port port-social" cx="486" cy="238" r="7"/></g>
    <g><circle class="port-outline" cx="615" cy="194" r="9"/><circle class="port port-social" cx="615" cy="194" r="7"/></g>
    <g><circle class="port-outline" cx="486" cy="614" r="9"/><circle class="port port-social" cx="486" cy="614" r="7"/></g>
    <g><circle class="port-outline" cx="615" cy="654" r="9"/><circle class="port port-social" cx="615" cy="654" r="7"/></g>
    <g><circle class="port-outline" cx="357" cy="440" r="9"/><circle class="port port-portal" cx="357" cy="440" r="7"/></g>
    <g><circle class="port-outline" cx="479" cy="358" r="9"/><circle class="port port-portal" cx="479" cy="358" r="7"/></g>
    <g><circle class="port-outline" cx="479" cy="491" r="9"/><circle class="port port-portal" cx="479" cy="491" r="7"/></g>
    <g><circle class="port-outline" cx="645" cy="108" r="9"/><circle class="port port-channel" cx="645" cy="108" r="7"/></g>
    <g><circle class="port-outline" cx="645" cy="740" r="9"/><circle class="port port-channel" cx="645" cy="740" r="7"/></g>
    <g><circle class="port-outline" cx="942" cy="424" r="9"/><circle class="port port-channel" cx="942" cy="424" r="7"/></g>
  </g>

  <g class="channels">
    <g class="channel" transform="translate(702,96)"><circle class="disc" r="36"/><rect class="glyph" role="img" aria-label="Product box icon" x="-12" y="-26" width="24" height="20" rx="4"/><text y="6">Products/</text><text y="14">Services Websites</text><text y="22">&amp; Pages</text></g>
    <g class="channel" transform="translate(803,51)"><circle class="disc" r="36"/><rect class="glyph" role="img" aria-label="Newspaper icon" x="-12" y="-24" width="24" height="20" rx="4"/><text y="10">Onsite News</text><text y="18">Pages</text></g>
    <g class="channel" transform="translate(869,116)"><circle class="disc" r="36"/><rect class="glyph" role="img" aria-label="Video player icon" x="-12" y="-24" width="24" height="20" rx="4"/><text y="10">Video/Movie</text><text y="18">Profiles</text></g>
    <g class="channel" transform="translate(767,162)"><circle class="disc" r="36"/><rect class="glyph" role="img" aria-label="Person with gear icon" x="-12" y="-26" width="24" height="20" rx="4"/><text y="6">Staff/Key</text><text y="14">Personnel</text><text y="22">Profiling</text></g>
    <g class="channel" transform="translate(934,182)"><circle class="disc" r="36"/><rect class="glyph" role="img" aria-label="Envelope with megaphone icon" x="-12" y="-24" width="24" height="20" rx="4"/><text y="10">Newsletter/Email</text><text y="18">Campaigns</text></g>
    <g class="channel" transform="translate(833,227)"><circle class="disc" r="36"/><rect class="glyph" role="img" aria-label="Laptop with code icon" x="-12" y="-26" width="24" height="20" rx="4"/><text y="6">Directories/</text><text y="14">Webmaster Listings</text><text y="22">&amp; Profiles</text></g>
    <g class="channel" transform="translate(999,246)"><circle class="disc" r="36"/><rect class="glyph" role="img" aria-label="Network nodes icon" x="-12" y="-26" width="24" height="20" rx="4"/><text y="6">High Value</text><text y="14">Industry Related</text><text y="22">Backlinks</text></g>
    <g class="channel" transform="translate(898,292)"><circle class="disc" r="36"/><rect class="glyph" role="img" aria-label="Target with arrow icon" x="-12" y="-24" width="24" height="20" rx="4"/><text y="10">Authority</text><text y="18">Domains</text></g>
    <g class="channel" transform="translate(1064,312)"><circle class="disc" r="36"/><rect class="glyph" role="img" aria-label="Document with magnifier icon" x="-12" y="-24" width="24" height="20" rx="4"/><text y="10">Competitor</text><text y="18">Content</text></g>
    <g class="channel" transform="translate(963,358)"><circle class="disc" r="36"/><rect class="glyph" role="img" aria-label="Gears icon" x="-12" y="-24" width="24" height="20" rx="4"/><text y="10">Industry Related</text><text y="18">Content</text></g>
    <g class="channel" transform="translate(1125,372)"><circle class="disc" r="36"/><rect class="glyph" role="img" aria-label="Speech bubbles icon" x="-12" y="-24" width="24" height="20" rx="4"/><text y="10">Ratings/Reviews</text><text y="18">Profiles</text></g>
    <g class="channel" transform="translate(1029,422)"><circle class="disc" r="36"/><rect class="glyph" role="img" aria-label="Group of people icon" x="-12" y="-24" width="24" height="20" rx="4"/><text y="10">Employment</text><text y="18">Profiles/Listings</text></g>
    <g class="channel" transform="translate(1125,472)"><circle class="disc" r="36"/><rect class="glyph" role="img" aria-label="Shield with tick icon" x="-12" y="-24" width="24" height="20" rx="4"/><text y="10">Classified/Open</text><text y="18">Site Listings</text></g>
    <g class="channel" transform="translate(963,488)"><circle class="disc" r="36"/><rect class="glyph" role="img" aria-label="Stacked photos icon" x="-12" y="-24" width="24" height="20" rx="4"/><text y="10">Photo Sharing</text><text y="18">Profiles</text></g>
    <g class="channel" transform="translate(1064,533)"><circle class="disc" r="36"/><rect class="glyph" role="img" aria-label="Globe with magnifier icon" x="-12" y="-24" width="24" height="20" rx="4"/><text y="10">Search Engine</text><text y="18">Profiles</text></g>
    <g class="channel" transform="translate(898,552)"><circle class="disc" r="36"/><rect class="glyph" role="img" aria-label="Clipboard icon" x="-12" y="-22" width="24" height="20" rx="4"/><text y="14">White Papers</text></g>
    <g class="channel" transform="translate(999,598)"><circle class="disc" r="36"/><rect class="glyph" role="img" aria-label="Web page layout icon" x="-12" y="-24" width="24" height="20" rx="4"/><text y="10">Wiki</text><text y="18">Pages</text></g>
    <g class="channel" transform="translate(833,618)"><circle class="disc" r="36"/><rect class="glyph" role="img" aria-label="Book with pen icon" x="-12" y="-22" width="24" height="20" rx="4"/><text y="14">Case Studies</text></g>
    <g class="channel" transform="translate(934,662)"><circle class="disc" r="36"/><rect class="glyph" role="img" aria-label="Pie chart icon" x="-12" y="-22" width="24" height="20" rx="4"/><text y="14">Info Graphics</text></g>
    <g class="channel" transform="translate(767,684)"><circle class="disc" r="36"/><rect class="glyph" role="img" aria-label="Chain link with tick icon" x="-12" y="-24" width="24" height="20" rx="4"/><text y="10">RSS</text><text y="18">Syndication</text></g>
    <g class="channel" transform="translate(869,729)"><circle class="disc" r="36"/><rect class="glyph" role="img" aria-label="Bar chart with trend line icon" x="-12" y="-24" width="24" height="20" rx="4"/><text y="10">Data/Analytics</text><text y="18">Sharing</text></g>
    <g class="channel" transform="translate(702,748)"><circle class="disc" r="36"/><rect class="glyph" role="img" aria-label="Monitor with chart icon" x="-12" y="-24" width="24" height="20" rx="4"/><text y="10">Static</text><text y="18">Websites</text></g>
    <g class="channel" transform="translate(803,794)"><circle class="disc" r="36"/><rect class="glyph" role="img" aria-label="Browser window icon" x="-12" y="-24" width="24" height="20" rx="4"/><text y="10">Web 2.0</text><text y="18">Pages</text></g>
  </g>
</svg>
</body>
</html>
```